Flyer For Commercial And Residential Seal Coating

Create a flyer so costumers know what type of services we offer. we would like to use all the info in the word documents if possible.any questions please ask. We want to give our customers as much information about of company and our products as possible. We are looking forward to seeing your designs

Target Market(s)

Business Owners, Home Owners, property managers

Industry/Entity Type

Construction Company

Font styles to use
Serif

Requirements
Must have
• Our Company Name. Phone Number, Email, Business Address we would like to have as much information on these flyers as possible
Nice to have
• we would like to have as much information on these flyers as possible
Should not have
• there are none

```html
<!DOCTYPE html>
<html lang="en">
<head>
<meta charset="utf-8">
<title>Northgate Pavement Care – Pothole Repair &amp; Sealcoating Brochure</title>
<link href="https://fonts.googleapis.com/css2?family=Exo+2:ital,wght@0,300;0,400;0,500;0,600;1,300&display=swap" rel="stylesheet">
<style>
  :root{
    --blue:#3f87cf;
    --blue-deep:#2f6fb5;
    --blue-light:#5b9be0;
    --ink:#2d2d2d;
    --ink-soft:#4a4a4a;
    --panel:#e5e4e2;
    --paper:#ffffff;
    --backdrop:#efefef;
    --white:#ffffff;
  }
  *{box-sizing:border-box;margin:0;padding:0}
  html,body{width:1200px;height:862px;overflow:hidden;background:var(--backdrop);font-family:"Exo 2",sans-serif;color:var(--ink)}
  .spread{position:absolute;left:50px;top:16px;width:1100px;height:830px;display:flex;box-shadow:0 6px 24px rgba(0,0,0,.12)}
  .page{position:relative;width:550px;height:830px;background:var(--paper);overflow:hidden}
  .page svg.bg{position:absolute;inset:0}
  .abs{position:absolute}
  p{font-size:6.6px;line-height:1.72;font-weight:300}
  h3{font-size:9.2px;font-weight:500;line-height:1.25;margin-bottom:5px}

  /* left page */
  .brand{left:38px;top:34px;color:var(--blue-deep);font-weight:600;font-size:17px;line-height:1.05;letter-spacing:.5px;display:flex;align-items:center;gap:8px}
  .brand-dot{width:12px;height:12px;border-radius:50%;background:var(--blue-deep)}
  .brand small{display:block;font-size:17px;font-weight:600}
  .hotline{right:28px;top:8px;text-align:right}
  .hotline .num{font-size:30px;font-weight:500;color:var(--blue);letter-spacing:.5px}
  .hotline .web{font-size:8px;font-weight:500;color:var(--ink-soft);margin-top:2px}
  .title-box{left:56px;background:var(--blue);color:var(--white);font-weight:500;padding:0 12px;display:flex;align-items:center;opacity:.95}
  .title-main{top:158px;height:45px;font-size:24px}
  .title-sub{top:210px;height:38px;font-size:16.5px}
  .intro{left:56px;top:256px;width:380px;color:var(--white);font-style:italic;font-size:8.6px;line-height:1.45}
  .blue-copy{left:20px;color:var(--white);width:250px}
  .blue-copy p{color:#eaf2fb}
  .who{left:326px;top:540px;width:208px}
  .who h2{font-size:14px;font-weight:400;margin-bottom:12px;color:var(--ink)}
  .who p{margin-bottom:10px;color:var(--ink-soft)}

  /* right page */
  .rp-blue{left:20px;color:var(--white);width:250px}
  .rp-blue p{color:#eaf2fb}
  .product{left:100px;top:410px;width:70px;height:58px;border-radius:35px/12px;background:linear-gradient(#4a403a,#2a2522)}
  .col-left{left:20px;top:492px;width:230px}
  .col-left p{color:var(--ink-soft);margin-bottom:12px}
  .col-right{left:290px;top:340px;width:250px}
  .col-right p{color:var(--ink-soft);margin-bottom:10px}
  .rules li{list-style:none;display:flex;gap:6px;font-size:6.6px;line-height:1.72;font-weight:300;color:var(--ink-soft);margin-bottom:9px}
  .rules li::before{content:"";flex:0 0 5px;height:5px;margin-top:3px;border-radius:50%;background:var(--blue)}
  .contact{left:262px;top:728px;width:280px}
  .contact-row{display:flex;align-items:center;gap:8px;margin-bottom:8px}
  .contact-icon{width:24px;height:24px;border-radius:50%;background:var(--blue);display:flex;align-items:center;justify-content:center;flex:0 0 24px}
  .contact-row .big{font-size:12px;font-weight:400;line-height:1.15}
  .contact-row .small{font-size:8px;font-weight:400}
</style>
</head>
<body>
<div class="spread">

  <!-- LEFT PAGE -->
  <section class="page page-left">
    <svg class="bg" width="550" height="830" viewBox="0 0 550 830">
      <rect width="550" height="830" fill="#f4f4f4"/>
      <rect x="0" y="100" width="550" height="420" fill="url(#paveGrad)"/>
      <polygon points="190,118 550,88 550,106 190,124" fill="var(--blue)"/>
      <polygon points="200,100 550,72 550,90 190,118" fill="var(--blue-light)" opacity=".55"/>
      <polygon points="0,260 296,505 296,830 0,830" fill="var(--blue)" opacity=".93"/>
      <rect x="296" y="505" width="254" height="325" fill="var(--paper)"/>
      <rect x="0" y="826" width="550" height="4" fill="var(--blue)"/>
      <defs>
        <linearGradient id="paveGrad" x1="0" y1="0" x2="1" y2="1">
          <stop offset="0" stop-color="#8d8f92"/>
          <stop offset=".5" stop-color="#6f7174"/>
          <stop offset="1" stop-color="#9a9b9d"/>
        </linearGradient>
      </defs>
    </svg>
    <div class="abs" role="img" aria-label="Photo of a worker spreading sealcoat on asphalt with a squeegee" style="left:0;top:100px;width:550px;height:160px"></div>

    <div class="abs brand"><span class="brand-dot"></span><div>NORTHGATE<small>PAVEMENT CARE</small></div></div>
    <div class="abs hotline">
      <div class="num">555-014-2870</div>
      <div class="web">www.northgatepavementcare.com</div>
    </div>

    <div class="abs title-box title-main">POTHOLE REPAIR</div>
    <div class="abs title-box title-sub">AVOIDING COSTLY LIABILITIES</div>
    <p class="abs intro">Moisture intrusion is the leading cause of pavement deterioration. When left alone and when cracks are not repaired, potholes become evident and a safety problem.</p>

    <div class="abs blue-copy" style="top:445px">
      <h3>Crack Sealing is an Integral Component of an Effective Pavement Preservation Program.</h3>
      <p>A scheduled program of pavement maintenance that includes sealcoating and crack filling will more than double the life cycle of your asphalt pavement and provide maximum curb appeal. Sealcoating and crack filling is a fraction of the cost of repairing or replacing asphalt pavement. The key to effective crack filling and sealing is to repair and fill the cracks while they are small, as crack filling inhibits crack growth and keeps new cracks from forming.</p>
    </div>
    <div class="abs blue-copy" style="top:578px;width:255px">
      <h3>Crack Sealing Provides Superior Protection Against Moisture Intrusion – The Leading Cause of Pavement Failure.</h3>
      <p>Left unfilled, cracks will allow rain and moisture to flow through pavement and erode base materials ultimately resulting in potholes and pavement failure. Filling cracks with crack filler helps prevent rain and moisture from flowing through the pavement and causing erosion or failure. By stopping the entrance of water, the rate of deterioration of the pavement is significantly slowed. Crack sealing also prevents the loss of aggregate from the edges of the crack.</p>
    </div>
    <div class="abs blue-copy" style="top:712px;width:255px">
      <h3>What is Hot Pour Crack Filling &amp; Sealing?</h3>
      <p>Hot pour cracking involves heated up blocks of rubberized asphalt in a specially designed oil-jacketed melter and then applying the heated material to cracks in roads and parking lots. Hot pour crack filling and sealing is generally done on roads and highways and in many cases, on parking lots. Hot pour offers the advantage of quick set times (10 minutes or less). Once the hot pour material cools you can drive on it.</p>
    </div>

    <div class="abs who">
      <h2>WHO ARE WE?</h2>
      <p>Northgate Pavement Care Inc. is a first generation family owned and operated asphalt maintenance company located in Riverton, New York. We specialize in residential asphalt maintenance and commercial asphalt maintenance. Our services include driveway asphalt seal coating, commercial asphalt seal coating, crack filling and asphalt patching.</p>
      <p>The biggest investment most people make in their lifetime is their home. Your driveway is the welcome mat to your home. Proper care and maintenance of the asphalt pavement is critical to protecting that investment. Northgate Pavement Care Inc. provides complete asphalt maintenance services in the Capital District to protect sure your investment using only the highest quality asphalt maintenance materials.</p>
      <p>We provide our clients in the Capital District with free written estimates for asphalt paving and we will schedule the work at a time that is most convenient for you. We will do the necessary asphalt maintenance preparations to your driveway or parking lot and our professional crew will get the job done right the first time. Our asphalt maintenance work is guaranteed and our clients satisfaction comes first.</p>
    </div>
  </section>

  <!-- RIGHT PAGE -->
  <section class="page page-right">
    <svg class="bg" width="550" height="830" viewBox="0 0 550 830">
      <rect width="550" height="830" fill="var(--paper)"/>
      <polygon points="262,318 550,248 550,715 262,715" fill="var(--panel)"/>
      <polygon points="0,0 550,0 550,255 0,130" fill="url(#houseGrad)"/>
      <polygon points="0,130 385,270 0,435" fill="var(--blue)"/>
      <polygon points="200,830 215,823 550,823 550,830" fill="var(--blue)"/>
      <defs>
        <linearGradient id="houseGrad" x1="0" y1="0" x2="0" y2="1">
          <stop offset="0" stop-color="#9cc2e6"/>
          <stop offset=".45" stop-color="#8a8476"/>
          <stop offset=".75" stop-color="#5e8a3e"/>
          <stop offset="1" stop-color="#2a2d33"/>
        </linearGradient>
      </defs>
    </svg>
    <div class="abs" role="img" aria-label="Photo of a large house with a freshly sealcoated driveway" style="left:0;top:0;width:550px;height:130px"></div>

    <div class="abs rp-blue" style="top:214px;width:240px">
      <h3>Pothole Repair – Avoiding Costly Liabilities</h3>
      <p>Moisture intrusion is the leading cause of pavement deterioration. When left alone and when cracks are not repaired, potholes become evident and a safety problem. Potholes represent an annoyance to vehicle traffic and a serious tripping hazard to pedestrians.</p>
    </div>
    <div class="abs rp-blue" style="top:289px;width:260px">
      <h3>To Properly Maintain a Driveway or Parking Lot, It's Important to Prepare the Asphalt Surface Prior to Sealcoating.</h3>
      <p style="width:170px">Cracks in your pavement along with pot holes and raveling not only reduce the value of your property and are un-appealing, they are also a safety issue and cause problems for visitors.</p>
    </div>

    <div class="abs product" role="img" aria-label="Photo of an asphalt core sample"></div>

    <div class="abs col-left">
      <h3>Asphalt Sealcoating is the Smart Choice for Pavement Preservation.</h3>
      <p>Asphalt pavement is mostly rock and/or stone and gravel, along with a binder. The rock, or aggregate, is held together with this binder known as asphalt cement. Maintaining this binder is essential to preserve the service life of asphalt surfaces. Rain, U.V. rays, and chemicals, as they are introduced into the asphalt, will degrade the binder and thus begin the degradation process of the asphalt. This will continue and create a surface that turns brittle. So, the purpose of asphalt sealcoating is to protect the asphalt pavement and to beautify at the same time. The earlier an asphalt sealer can be applied in the life cycle of asphalt the better.</p>
      <h3>Sealcoating Increases Pavement Service Life</h3>
      <p>To reduce the effects of the above-mentioned elements, it is important to implement a maintenance program that utilizes sealcoating to extend the life of your parking lot or driveway. Sealcoating will provide a layer of protection blocking out harmful intrusions such as water, oils, and U.V. damage. In addition, when asphalt sealer is applied to manufacturers' specifications, sealcoating provides a slip-resistant surface with a deep black finish that beautifies the parking lot or driveway. Asphalt sealers are typically bituminous based products or acrylics. The sealcoat is in a liquid formulation of one of the above emulsions, mixed with water, silica sand, polymer additives, and other proprietary fillers and solids. These products can be applied by brush, spray or squeegee.</p>
    </div>

    <div class="abs col-right">
      <h3>What is Asphalt Pavement?</h3>
      <p>Asphalt Pavement, also known as Hot Mix, is a simple blend of two main components; Molten Liquid Asphalt (the black glue or binder), and Crushed Rock or Aggregate. The Hot Mix is then placed and compacted to form asphalt pavement.</p>
      <h3>Your Parking Lot is the "Welcome Mat" to Your Property.</h3>
      <p>It provides both image and functionality to business or institution. Your parking lot represents a substantial capital investment that must be maintained.</p>
      <p>A scheduled program of pavement maintenance that includes sealcoating and crack filling will more than double the life of your asphalt pavement and provide maximum curb appeal.</p>
      <p>Sealcoating and crack filling are a fraction of the cost of repairing or replacing asphalt pavement.</p>
      <h3>Rules For Applying Asphalt Sealcoating</h3>
      <p>When applying a sealcoating product, follow the important steps referenced below to get the most protection and optimum performance:</p>
      <ul class="rules">
        <li>Temperatures must be a minimum of 50 degrees and rising for a period of not less than 24 hours. Do not apply when temperatures are forecasted to get below the 50-degree mark.</li>
        <li>Do not apply if rain is imminent within the same 24-hour period.</li>
        <li>Once finished with the application of sealcoat, allow to cure 24 hours before allowing vehicle traffic back on the surface.</li>
      </ul>
    </div>

    <div class="abs contact">
      <div class="contact-row">
        <span class="contact-icon">
          <svg width="12" height="12" viewBox="0 0 12 12"><path d="M6 1a3.5 3.5 0 0 0-3.5 3.5C2.5 7.5 6 11 6 11s3.5-3.5 3.5-6.5A3.5 3.5 0 0 0 6 1zm0 4.8a1.3 1.3 0 1 1 0-2.6 1.3 1.3 0 0 1 0 2.6z" fill="#fff"/></svg>
        </span>
        <div class="big">48 Linden Court<br>Riverton New York 12000</div>
      </div>
      <div class="contact-row">
        <span class="contact-icon">
          <svg width="12" height="12" viewBox="0 0 12 12"><path d="M10.5 1.5 1.5 5.2l3.4 1.3 1.3 3.5 4.3-8.5zM4.9 6.5l3.5-2.8" fill="none" stroke="#fff" stroke-width="1" stroke-linejoin="round"/></svg>
        </span>
        <div><div class="big">555-014-2870</div><div class="small">hello@northgatepavementcare.com</div></div>
      </div>
    </div>
  </section>

</div>
</body>
</html>
```